VENTURE CAPITAL GROUP BUSINESS CARD DESIGN

Venture Capital Group based in SF looking for a bold business card design. No trendy colour explosion, 3D effects etc. Just "simple" optical effects. Works on your brain, keeps your eye focused and sticks to your mind.
Target Market(s)
Technology startups
Industry/Entity Type
Venture Capital
Contact Information for Business Card
BARTHOLOMEW ELLING
MANAGING PARTNER
817 FERN ST SAN FRANCISCO, CA 94111
415.555.0142 O
415.555.0187 F
415.555.0236 C
bart@quillbrookfunds.example

```html
<!DOCTYPE html>
<html lang="en">
<head>
<meta charset="utf-8">
<title>Quillbrook Funds — Business Card</title>
<link href="https://fonts.googleapis.com/css2?family=Open+Sans:wght@400;600;700&display=swap" rel="stylesheet">
<style>
  :root {
    --backdrop: #3b3431;
    --green-light: #4fb556;
    --green-mid: #2f9a3c;
    --green-dark: #16702a;
    --brand-green: #2a9b3a;
    --card-black: #050505;
    --ink-white: #ffffff;
    --ink-soft: #e6f3e7;
  }
  html, body {
    margin: 0;
    padding: 0;
    width: 1200px;
    height: 844px;
    overflow: hidden;
    background: var(--backdrop);
    font-family: "Open Sans", Arial, sans-serif;
  }
  .stage {
    position: relative;
    width: 1200px;
    height: 844px;
  }
  .card {
    position: absolute;
    top: 272px;
    width: 520px;
    height: 300px;
    border-radius: 3px;
    box-shadow: 0 10px 28px rgba(0,0,0,0.45);
    overflow: hidden;
  }
  /* Front: contact side */
  .card--front {
    left: 50px;
    background: linear-gradient(150deg, var(--green-light) 0%, var(--green-mid) 50%, var(--green-dark) 100%);
    color: var(--ink-white);
  }
  .contact {
    position: absolute;
    right: 28px;
    top: 28px;
    text-align: right;
    line-height: 1.35;
  }
  .contact__name {
    font-size: 17px;
    font-weight: 700;
    margin: 0;
  }
  .contact__title {
    font-size: 13px;
    color: var(--ink-soft);
    margin: 0 0 12px;
  }
  .contact__address {
    font-size: 13px;
    color: var(--ink-soft);
    margin: 0;
  }
  .contact__lines {
    list-style: none;
    margin: 6px 0 0;
    padding: 0;
    font-size: 13px;
  }
  .contact__lines li {
    display: flex;
    justify-content: flex-end;
    align-items: center;
    gap: 6px;
  }
  .contact__lines svg {
    width: 11px;
    height: 11px;
    fill: var(--ink-white);
  }
  .contact__email {
    position: absolute;
    right: 28px;
    top: 196px;
    font-size: 13px;
    margin: 0;
  }
  .brand-name {
    position: absolute;
    right: 28px;
    bottom: 34px;
    margin: 0;
    font-size: 28px;
    font-weight: 600;
    letter-spacing: 1px;
    color: var(--ink-white);
  }
  /* Back: brand side */
  .card--back {
    left: 630px;
    background: var(--card-black);
    display: flex;
    flex-direction: column;
    align-items: center;
    justify-content: center;
    gap: 22px;
  }
  .brand-dot {
    width: 64px;
    height: 64px;
    border-radius: 50%;
    background: var(--brand-green);
  }
  .card--back .brand-name {
    position: static;
    font-size: 34px;
    color: var(--brand-green);
  }
</style>
</head>
<body>
<main class="stage">
  <section class="card card--front" aria-label="Card front with contact details">
    <div class="contact">
      <p class="contact__name">Bartholomew Elling</p>
      <p class="contact__title">Managing Partner</p>
      <p class="contact__address">817 Fern St<br>San Francisco, CA 94111</p>
      <ul class="contact__lines">
        <li>415.555.0142
          <svg viewBox="0 0 24 24" aria-label="Office"><path d="M6.6 10.8a15 15 0 0 0 6.6 6.6l2.2-2.2a1 1 0 0 1 1-.25 11.4 11.4 0 0 0 3.6.57 1 1 0 0 1 1 1V20a1 1 0 0 1-1 1A17 17 0 0 1 3 4a1 1 0 0 1 1-1h3.5a1 1 0 0 1 1 1c0 1.25.2 2.45.57 3.57a1 1 0 0 1-.25 1z"/></svg>
        </li>
        <li>415.555.0187
          <svg viewBox="0 0 24 24" aria-label="Fax"><path d="M6 2h9l3 3v5H6zM3 11h18v9H3zm3 2v2h4v-2zm0 3v2h4v-2zm8-3v5h4v-5z"/></svg>
        </li>
        <li>415.555.0236
          <svg viewBox="0 0 24 24" aria-label="Mobile"><path d="M7 1h10a2 2 0 0 1 2 2v18a2 2 0 0 1-2 2H7a2 2 0 0 1-2-2V3a2 2 0 0 1 2-2zm0 3v14h10V4zm5 15.5a1 1 0 1 0 0 2 1 1 0 0 0 0-2z"/></svg>
        </li>
      </ul>
    </div>
    <p class="contact__email">bart@quillbrookfunds.example
      <svg viewBox="0 0 24 24" width="11" height="11" fill="#fff" aria-label="Email"><path d="M2 5h20v14H2zm2 2v.5l8 5 8-5V7zm0 3v7h16v-7l-8 5z"/></svg>
    </p>
    <p class="brand-name">QUILLBROOK FUNDS</p>
  </section>

  <section class="card card--back" aria-label="Card back with company name">
    <div class="brand-dot"></div>
    <p class="brand-name">QUILLBROOK FUNDS</p>
  </section>
</main>
</body>
</html>
```